Business Card Design Project

I need a business card design for an Organic drive thru coffee kiosk. We will serve organic coffee, teas & smoothies and will serve healthy breakfast food/snacks for people on the go.
I want the card to have 2-3 colors max (earthy colors like browns, greens and so on).
I have attached the logo I want used and would love to play off the theme of "balance."
Include:
Tidy-Kettle Coffee
address: 4820 Gorvin Ct. Larkmont, OR 27583
phone: 503-731-4062
website: www.tidy-kettle.com (website is not up yet but still include it on card)
email: Rosalind@tidy-kettle.com
I want one of the following sayings somewhere on the card (the front or back is fine):
"Sip & Snack Right, on the go!"
"Break the fast with Tidy-Kettle"
Maybe on the back list what we offer:
-Organic coffee, espresso & tea
-Blendora smoothies & protein shakes
-Zesty Pour (100% fresh local fruit and veggies)
-Tender Nibs

```html
<!DOCTYPE html>
<html lang="en">
<head>
<meta charset="utf-8">
<title>Tidy-Kettle Coffee — Business Card</title>
<link rel="stylesheet" href="https://fonts.googleapis.com/css2?family=Open+Sans:wght@400;600&family=Ubuntu:wght@400;500;700&display=swap">
<style>
  :root {
    --page: #ffffff;
    --card-light: #ffffff;
    --card-shade: #dedede;
    --leaf: #3b5404;
    --night: #1c1c1c;
    --roast: #3a2213;
    --bean: #7a3a22;
    --cream: #ffffff;
  }
  * { margin: 0; padding: 0; box-sizing: border-box; }
  html, body { width: 1200px; height: 1000px; overflow: hidden; background: var(--page); }
  body { position: relative; font-family: "Ubuntu", sans-serif; color: var(--cream); }

  .card {
    position: absolute; left: 200px; width: 844px; height: 494px;
    border-radius: 10px; overflow: hidden;
    background: radial-gradient(ellipse 70% 80% at 50% 55%, var(--card-light) 55%, var(--card-shade) 100%);
  }
  .card--front { top: 0; }
  .card--back { top: 494px; }

  .brand { position: absolute; left: 0; right: 0; top: 58px; text-align: center; }
  .brand__dot {
    display: block; margin: 0 auto 12px; width: 80px; height: 80px;
    border-radius: 50%; background: var(--bean);
  }
  .brand__name {
    font-family: "Ubuntu", sans-serif; font-weight: 500; font-size: 58px;
    color: var(--roast); line-height: 1; letter-spacing: -1px;
  }

  .slogan-band {
    position: absolute; left: 0; right: 0; top: 277px; bottom: 0;
    background: var(--leaf);
    display: flex; flex-direction: column; justify-content: center; align-items: center;
    font-family: "Open Sans", sans-serif; font-size: 27px; line-height: 46px;
    padding-bottom: 4px;
  }

  .offer-band {
    position: absolute; left: 0; right: 0; top: 337px; height: 56px;
    background: var(--leaf); display: flex; align-items: center;
  }
  .offer-band__title { font-weight: 500; font-size: 19px; letter-spacing: 0.8px; margin-left: 29px; width: 159px; }
  .offer-band__list {
    border-left: 3px solid var(--cream); padding-left: 14px;
    font-size: 12.5px; font-weight: 500; letter-spacing: 0.7px; line-height: 20px;
  }
  .offer-band__list--first { width: 292px; }

  .contact-band {
    position: absolute; left: 0; right: 0; top: 393px; bottom: 0;
    background: var(--night); font-size: 12px; font-weight: 500;
  }
  .contact { position: absolute; display: flex; align-items: flex-start; gap: 17px; }
  .contact svg { width: 18px; height: 18px; flex: none; fill: var(--cream); }
  .contact--web { font-size: 14px; gap: 12px; }
  .contact--address { line-height: 23px; font-size: 11.5px; gap: 12px; }
</style>
</head>
<body>

  <section class="card card--front">
    <div class="brand">
      <span class="brand__dot"></span>
      <div class="brand__name">Tidy-Kettle</div>
    </div>
    <div class="slogan-band">
      <p>"Sip &amp; Snack Right, on the go!"</p>
      <p>"Break the fast with Tidy-Kettle"</p>
    </div>
  </section>

  <section class="card card--back">
    <div class="brand">
      <span class="brand__dot"></span>
      <div class="brand__name">Tidy-Kettle</div>
    </div>

    <div class="offer-band">
      <div class="offer-band__title">What we offer</div>
      <div class="offer-band__list offer-band__list--first">
        <p>Organic coffee, espresso &amp; tea</p>
        <p>Blendora smoothies &amp; protein shakes</p>
      </div>
      <div class="offer-band__list">
        <p>Zesty Pour (100% fresh local fruit and veggies)</p>
        <p>Tender Nibs</p>
      </div>
    </div>

    <div class="contact-band">
      <div class="contact" style="left:58px; top:12px;">
        <svg viewBox="0 0 18 18"><rect x="2" y="2" width="5" height="14" rx="1"/><rect x="8" y="4" width="9" height="12" rx="1"/><rect x="10" y="6" width="5" height="2" fill="#1c1c1c"/><rect x="10" y="10" width="5" height="4" fill="#1c1c1c"/></svg>
        <span>503-731-4062</span>
      </div>
      <div class="contact" style="left:58px; top:42px;">
        <svg viewBox="0 0 18 18"><rect x="4" y="1" width="10" height="5"/><rect x="1" y="6" width="16" height="7" rx="1"/><rect x="4" y="11" width="10" height="6" fill="#fff" stroke="#1c1c1c" stroke-width="1"/></svg>
        <span>0 412 836 597</span>
      </div>
      <div class="contact" style="left:58px; top:72px;">
        <svg viewBox="0 0 18 18"><rect x="1" y="4" width="16" height="11"/><path d="M1 4 L9 11 L17 4" fill="none" stroke="#1c1c1c" stroke-width="1.5"/></svg>
        <span>Rosalind@tidy-kettle.com</span>
      </div>
      <div class="contact contact--web" style="left:511px; top:10px;">
        <svg viewBox="0 0 18 18"><circle cx="9" cy="9" r="8"/><path d="M5 5 Q8 6 7 9 Q6 12 9 14 M11 3 Q13 6 12 8 Q14 10 15 9" fill="none" stroke="#1c1c1c" stroke-width="1.5"/></svg>
        <span>www.tidy-kettle.com</span>
      </div>
      <div class="contact contact--address" style="left:511px; top:41px;">
        <svg viewBox="0 0 18 18"><path d="M9 1 A6 6 0 0 1 15 7 C15 11 9 17 9 17 C9 17 3 11 3 7 A6 6 0 0 1 9 1 Z"/><circle cx="9" cy="7" r="2.3" fill="#1c1c1c"/></svg>
        <span>Address&nbsp; 4820 Gorvin Ct. Larkmont, OR 27583<br>Meltem&nbsp; WA 24680 DORVALE</span>
      </div>
    </div>
  </section>

</body>
</html>
```